Brindlewood Business Card Design

Small Company
looking to ramp up work need business cards sick of everyone asking for a card
client base is broad.
keep it simple
Just want on the reverse of the card somewhere for me to write details for clients
appointments etc..
want to use the phrase
"Your safe, reliable and trust worthy Tradesmen"

Industry/Entity Type

Business

Contact Information for Business Card

Brindlewood Electrical Solutions Pty Ltd
Director Gregory Brindlewood
email - brindlewoodelectricalsolutions@zentromail.net
Ph - 03 95418276
Mobile - 0417592836
Domestic, Industrial, Commercial & Mining
Electrical, Solar, Communications & Fibre
REC: 41873

```html
<!DOCTYPE html>
<html lang="en">
<head>
<meta charset="utf-8">
<title>Brindlewood Electrical Solutions – Business Card</title>
<link href="https://fonts.googleapis.com/css2?family=Questrial&display=swap" rel="stylesheet">
<style>
  :root {
    --brand-blue: #2b3c94;
    --brand-red: #e8202a;
    --paper: #ffffff;
    --line-blue: #3a4aa0;
    --stage: #ecebe7;
  }
  * { margin: 0; padding: 0; box-sizing: border-box; }
  html, body { width: 1200px; height: 784px; overflow: hidden; }
  body {
    background: var(--stage);
    font-family: "Questrial", "Century Gothic", sans-serif;
    position: relative;
  }
  .card {
    position: absolute;
    width: 540px;
    height: 330px;
    top: 227px;
    overflow: hidden;
    box-shadow: 0 3px 10px rgba(0,0,0,0.18);
  }
  .card-back { left: 40px; background: var(--brand-blue); }
  .card-front { left: 620px; background: var(--paper); }

  /* Back */
  .services {
    position: absolute; top: 22px; left: 0; width: 100%;
    text-align: center; color: var(--paper); font-size: 15px; line-height: 1.25;
  }
  .services .licence { color: var(--brand-red); font-size: 12px; letter-spacing: 0.5px; }
  .notes-box {
    position: absolute; left: 50px; top: 84px; width: 440px; height: 210px;
    background: var(--paper);
  }
  .notes-watermark {
    position: absolute; left: 0; top: 62px; width: 100%; text-align: center;
    font-size: 58px; color: var(--brand-blue); opacity: 0.1;
  }
  .notes-lines { position: absolute; inset: 0; }

  /* Front */
  .front-art { position: absolute; inset: 0; }
  .holder { position: absolute; top: 30px; right: 28px; text-align: right; }
  .holder-name { color: var(--brand-blue); font-size: 15px; }
  .holder-title { color: var(--brand-red); font-size: 12px; }
  .brand {
    position: absolute; left: 32px; top: 84px;
    display: flex; align-items: center; gap: 10px;
  }
  .brand-dot { width: 16px; height: 16px; border-radius: 50%; background: var(--brand-red); }
  .brand-name { color: var(--brand-blue); font-size: 40px; line-height: 1; }
  .tagline {
    position: absolute; left: 16px; top: 191px;
    color: var(--paper); font-size: 13px; line-height: 18px; letter-spacing: 2px;
    white-space: nowrap;
    transform: rotate(-4.2deg); transform-origin: left center;
  }
  .contacts { position: absolute; left: 26px; bottom: 22px; list-style: none; }
  .contacts li {
    display: flex; align-items: center; gap: 9px;
    color: var(--paper); font-size: 16px; line-height: 25px;
  }
  .contacts svg { width: 16px; height: 16px; flex: none; }
</style>
</head>
<body>

<section class="card card-back" aria-label="Business card reverse">
  <p class="services">
    Domestic, Industrial, Commercial &amp; Mining Electrical,<br>
    Solar, Communications &amp; Fibre<br>
    <span class="licence">REC: 41873</span>
  </p>
  <div class="notes-box">
    <div class="notes-watermark" aria-hidden="true">Brindlewood</div>
    <svg class="notes-lines" viewBox="0 0 440 210" aria-hidden="true">
      <g stroke="var(--line-blue)" stroke-width="1" stroke-dasharray="4 3">
        <line x1="8" y1="30" x2="432" y2="30"/>
        <line x1="8" y1="55" x2="432" y2="55"/>
        <line x1="8" y1="80" x2="432" y2="80"/>
        <line x1="8" y1="105" x2="432" y2="105"/>
        <line x1="8" y1="130" x2="432" y2="130"/>
        <line x1="8" y1="155" x2="432" y2="155"/>
        <line x1="8" y1="180" x2="432" y2="180"/>
        <line x1="8" y1="202" x2="432" y2="202"/>
      </g>
    </svg>
  </div>
</section>

<section class="card card-front" aria-label="Business card front">
  <svg class="front-art" viewBox="0 0 540 330" aria-hidden="true">
    <polygon points="0,210 540,170 540,330 0,330" fill="var(--brand-blue)"/>
    <polygon points="0,190 540,150 540,170 0,210" fill="var(--brand-red)"/>
  </svg>

  <div class="holder">
    <div class="holder-name">Gregory Brindlewood</div>
    <div class="holder-title">Director</div>
  </div>

  <div class="brand">
    <span class="brand-dot" aria-hidden="true"></span>
    <span class="brand-name">Brindlewood</span>
  </div>

  <p class="tagline">Your safe, reliable and trust worthy Tradesmen</p>

  <ul class="contacts">
    <li>
      <svg viewBox="0 0 16 16" aria-hidden="true"><path d="M3 1.5l3 2.5-1.3 2.2c.9 2 2.2 3.4 4.2 4.3L11 9.2l3 3-1.6 2.4C7 14 2 9 1.4 3.3z" fill="var(--brand-red)"/></svg>
      03 95418276
    </li>
    <li>
      <svg viewBox="0 0 16 16" aria-hidden="true"><rect x="4" y="1" width="8" height="14" rx="1.5" fill="var(--brand-red)"/><rect x="5.5" y="3" width="5" height="7" fill="var(--brand-blue)"/></svg>
      0417592836
    </li>
    <li>
      <svg viewBox="0 0 16 16" aria-hidden="true"><rect x="1" y="3" width="14" height="10" rx="1" fill="var(--brand-red)"/><path d="M1.5 3.5L8 9l6.5-5.5" stroke="var(--paper)" stroke-width="1.2" fill="none"/></svg>
      brindlewoodelectricalsolutions@zentromail.net
    </li>
  </ul>
</section>

</body>
</html>
```